Postcard flyer for body postive dance classes

We need an eye catching double sided A6 postcard for body positive dance classes. The business name is twirlbrightday and already have a rough logo and some text that needs tidying up and putting together. The design needs to be simple and elegant. We are appealing to a diverse range of adult women with or without dance experience to join us in a safe, supportive and creative environment. We would like the design to use black, white and a soft green. The final design should communicate movement, contentment and wholeness. File with information attached.

Target Market(s)

Diverse range of adult women

Industry/Entity Type

Health And Wellness

Font styles to use
Other font styles liked:
• Candara or similar but open to suggestions

Colors
abd036
cadf82
eaf2ce
fffefb
fef9ed
fff3d1
ffffff

Requirements
Must have
• Logo and text provided.
Nice to have
• Sense of movement. Match to website colours and style.
Should not have
• Intimidating perfect body images

```html
<!DOCTYPE html>
<html lang="en">
<head>
<meta charset="utf-8">
<title>twirlbrightday postcard</title>
<link rel="stylesheet" href="https://fonts.googleapis.com/css2?family=Allura&family=Satisfy&family=Mulish:wght@400&display=swap">
<style>
  :root {
    --page: #eef5f9;
    --sage: #a2ab87;
    --sage-band: rgba(160, 170, 128, 0.78);
    --sage-text: #a3ad85;
    --mark: #454c3e;
    --white: #ffffff;
    --cream: #f8f4ea;
    --paper: #fcfbf7;
    --ink: #1f1f1f;
  }
  * { box-sizing: border-box; margin: 0; padding: 0; }
  html, body { width: 892px; height: 1200px; overflow: hidden; }
  body {
    background: var(--page);
    position: relative;
    font-family: "Mulish", "Avenir", sans-serif;
  }
  .card { position: absolute; left: 112px; width: 662px; height: 468px; }
  .card-front { top: 70px; background: var(--sage); }
  .brand-mark {
    position: absolute; left: 50%; top: 176px;
    width: 140px; height: 140px; margin-left: -70px;
    transform: translateY(-106px);
  }
  .tagline {
    position: absolute; left: 0; right: 0; top: 300px;
    text-align: center; color: var(--white);
    font-family: "Satisfy", cursive; font-size: 34px; letter-spacing: 0.5px;
  }
  .brand-name {
    position: absolute; left: 0; right: 0; top: 370px;
    text-align: center; color: var(--white);
    font-size: 42px; font-weight: 400;
  }
  .card-back { top: 598px; background: var(--white); }
  .panel-left { position: absolute; left: 21px; top: 16px; width: 331px; height: 436px; background: var(--cream); }
  .panel-right { position: absolute; left: 352px; top: 16px; width: 251px; height: 436px; background: var(--paper); }
  .panel-edge { position: absolute; left: 603px; top: 16px; width: 37px; height: 436px; background: var(--cream); }
  .headline {
    position: absolute; left: 0; top: 0; width: 352px; height: 352px;
    font-family: "Allura", cursive; color: var(--sage-text);
  }
  .headline span { position: absolute; white-space: nowrap; line-height: 1; }
  .hl-big { font-size: 76px; }
  .hl-small { font-size: 50px; }
  .hl-1 { left: 64px; top: 44px; }
  .hl-2 { left: 142px; top: 110px; }
  .hl-3 { left: 62px; top: 196px; }
  .hl-4 { left: 142px; top: 262px; }
  .intro {
    position: absolute; left: 374px; top: 84px; width: 207px;
    text-align: center; color: var(--ink);
    font-size: 15.5px; line-height: 1.2;
  }
  .intro p + p { margin-top: 36px; }
  .contact-band {
    position: absolute; left: 0; top: 352px; width: 662px; height: 72px;
    background: var(--sage-band); color: var(--white);
    display: flex; flex-direction: column; justify-content: center;
    align-items: center; font-size: 16px; line-height: 1.35;
    padding-right: 36px;
  }
</style>
</head>
<body>
  <section class="card card-front">
    <svg class="brand-mark" viewBox="0 0 140 140" aria-hidden="true">
      <circle cx="70" cy="70" r="62" fill="none" stroke="var(--mark)" stroke-width="5"/>
    </svg>
    <p class="tagline">movement, contentment, wholeness</p>
    <h1 class="brand-name">twirlbrightday</h1>
  </section>

  <section class="card card-back">
    <div class="panel-left"></div>
    <div class="panel-right"></div>
    <div class="panel-edge"></div>
    <h2 class="headline">
      <span class="hl-big hl-1">Dance</span>
      <span class="hl-small hl-2">is joy,</span>
      <span class="hl-big hl-3">dance</span>
      <span class="hl-small hl-4">is love</span>
    </h2>
    <div class="intro">
      <p>Dance is at the core of our being, a celebration of movement, vitality and wholeness.</p>
      <p>If you’ve never danced before and always wanted to or you want&nbsp; to reignite your past love of dance, join us at twirlbrightday to start your journey.</p>
    </div>
    <div class="contact-band">
      <span>E: hello@twirlbrightday.com.au - P: 0400518264</span>
      <span>www.twirlbrightday.com.au - Lindenvale/Ashcombe</span>
    </div>
  </section>
</body>
</html>
```